QM Regulatory Pathways - Biz Card - Re-do

I would like a re-do on my business card.

See my Internet site - qmregpathways.example

1) Remove direct phone line.
2) Add company moto - integrity, diligence, and excellence
3) Add Consulting Services listing:
-Benefit Technology
-ERISA Compliance
-Contract/Vendor Management
-Human Resource/Payroll
-Medical/Prescription Drug
-Integrated Leave of Absence

Target Market(s)

Employee benefit consulting and insurance purchasers, Usually human resource executives

Industry/Entity Type

Human Resource

Contact Information for Business Card

Same business card color scheme, logo,

Font styles to use
Sans Serif

Requirements
Must have
• Same color scheme and logo. Remove direct phone number. Keep all numbers, internet address.

```html
<!DOCTYPE html>
<html lang="en">
<head>
<meta charset="utf-8">
<title>QM Regulatory Pathways — Business Card</title>
<link rel="stylesheet" href="https://fonts.googleapis.com/css2?family=Montserrat:wght@400;500;600&display=swap">
<style>
  :root {
    --plum: #6a1e46;
    --slate: #65666b;
    --white: #ffffff;
    --soft-white: #f1e9ee;
    --rule: rgba(255,255,255,0.35);
    --backdrop: #dcdde0;
  }
  * { margin: 0; padding: 0; box-sizing: border-box; }
  html, body { width: 1200px; height: 800px; overflow: hidden; }
  body {
    background: var(--backdrop);
    font-family: "Montserrat", sans-serif;
    position: relative;
  }
  .card {
    position: absolute;
    top: 250px;
    width: 525px;
    height: 300px;
    color: var(--white);
    box-shadow: 0 6px 18px rgba(0,0,0,0.12);
  }
  .card--contact { left: 50px; background: var(--plum); }
  .card--brand { left: 625px; background: var(--slate); }

  .contact-list {
    position: absolute;
    left: 44px;
    top: 60px;
    list-style: none;
    font-size: 13px;
    line-height: 22px;
    color: var(--soft-white);
  }
  .contact-list li { display: flex; align-items: center; gap: 10px; }
  .contact-list svg { width: 12px; height: 12px; fill: var(--soft-white); flex: none; }
  .contact-address { margin-top: 6px; }

  .brand-mark {
    position: absolute;
    right: 48px;
    top: 92px;
    display: flex;
    flex-direction: column;
    align-items: center;
    gap: 10px;
  }
  .brand-dot { width: 78px; height: 78px; border-radius: 50%; background: var(--white); }
  .brand-name-small { font-size: 11px; font-weight: 500; letter-spacing: 0.04em; color: var(--white); }

  .person {
    position: absolute;
    right: 48px;
    bottom: 34px;
    text-align: right;
  }
  .person-name { font-size: 20px; font-weight: 400; }
  .person-title { font-size: 14px; color: var(--soft-white); margin-top: 2px; }

  .brand-lockup {
    position: absolute;
    left: 0; right: 0;
    top: 34px;
    display: flex;
    align-items: center;
    justify-content: center;
    gap: 14px;
  }
  .brand-lockup .brand-dot { width: 52px; height: 52px; background: var(--plum); }
  .brand-name { font-size: 23px; font-weight: 400; letter-spacing: 0.01em; color: var(--white); }
  .motto {
    position: absolute;
    left: 0; right: 0;
    top: 104px;
    text-align: center;
    font-size: 12px;
    letter-spacing: 0.04em;
    color: var(--soft-white);
  }
  .motto-dot { margin: 0 8px; }

  .services {
    position: absolute;
    left: 56px; right: 56px;
    top: 142px;
    border-top: 1px solid var(--rule);
    padding-top: 16px;
  }
  .services-title {
    text-align: center;
    font-size: 11px;
    font-weight: 600;
    letter-spacing: 0.14em;
    text-transform: uppercase;
    color: var(--white);
    margin-bottom: 12px;
  }
  .services-list {
    list-style: none;
    display: grid;
    grid-template-columns: 1fr 1fr;
    column-gap: 24px;
    row-gap: 8px;
    font-size: 12px;
    color: var(--soft-white);
  }
  .services-list li { display: flex; align-items: center; gap: 8px; white-space: nowrap; }
  .services-list li::before {
    content: "";
    width: 6px; height: 6px;
    border-radius: 50%;
    background: var(--plum);
    flex: none;
  }
</style>
</head>
<body>
  <section class="card card--contact" aria-label="Card front with contact details">
    <ul class="contact-list">
      <li>
        <svg viewBox="0 0 12 12" aria-hidden="true"><path d="M3 0h6v3H3zM1 4h10v5H9v3H3V9H1zM4 8v3h4V8z"/></svg>
        555.010.4822
      </li>
      <li>
        <svg viewBox="0 0 12 12" aria-hidden="true"><path d="M0 2h12v8H0zM1 3l5 4 5-4v-.2H1z" fill-rule="evenodd"/></svg>
        dferris@qmregpathways.example
      </li>
      <li>
        <svg viewBox="0 0 12 12" aria-hidden="true"><circle cx="6" cy="6" r="6"/></svg>
        qmregpathways.example
      </li>
      <li class="contact-address">410 Harbor Street NW, Suite 300</li>
      <li>Lakeview, MI 49000</li>
    </ul>

    <div class="brand-mark">
      <span class="brand-dot" aria-hidden="true"></span>
      <span class="brand-name-small">QM Regulatory Pathways</span>
    </div>

    <div class="person">
      <p class="person-name">Daniel Ferris</p>
      <p class="person-title">President</p>
    </div>
  </section>

  <section class="card card--brand" aria-label="Card back with company name, motto and services">
    <div class="brand-lockup">
      <span class="brand-dot" aria-hidden="true"></span>
      <span class="brand-name">QM Regulatory Pathways</span>
    </div>
    <p class="motto">Integrity<span class="motto-dot">•</span>Diligence<span class="motto-dot">•</span>and Excellence</p>

    <div class="services">
      <p class="services-title">Consulting Services</p>
      <ul class="services-list">
        <li>Benefit Technology</li>
        <li>Human Resource/Payroll</li>
        <li>ERISA Compliance</li>
        <li>Medical/Prescription Drug</li>
        <li>Contract/Vendor Management</li>
        <li>Integrated Leave of Absence</li>
      </ul>
    </div>
  </section>
</body>
</html>
```